Red Kettle Pictures BIz Card

This will be a biz card for our independent film company
RED KETTLE PICTURES

we have a logo and i need to figure out how to post it to you!

Here is the info we need on the card:

LOGO

dorianne pasko (lower case!)
dP@RedKettlePix.example
407-555-0148

Red Kettle Pictures, LLC
www.RedKettlePix.example

stories that matter (tagline)

Target Market(s)

adults in the entertainment industry in USA.
need something creative feeling, a bit funky, not to overt.
something eye catchy that people will be inclined to keep.

ask me any questions you have!

Industry/Entity Type

It Company

Requirements
Must have
• good looking! clean and easy to get the contact info. not too busy.
Nice to have
• love the cards where the design is "continued" on the back side.

perhaps the tag and logo on the back side?!?

open to ideas!
Should not have
• nothing "cartoonish"

```html
<!DOCTYPE html>
<html lang="en">
<head>
<meta charset="utf-8">
<title>Red Kettle Pictures – Business Card</title>
<link href="https://fonts.googleapis.com/css2?family=Didact+Gothic&family=Open+Sans:wght@400&family=Arimo:wght@400&display=swap" rel="stylesheet">
<style>
  :root {
    --ink: #000000;
    --paper: #ffffff;
    --amber: #f6b12a;
    --kettle-red: #e3201b;
    --reel-dark: #2a2a2a;
    --reel-light: #cfcfcf;
  }
  html, body {
    margin: 0;
    width: 1200px;
    height: 900px;
    overflow: hidden;
    background: var(--paper);
  }
  .canvas { position: relative; width: 1200px; height: 900px; }

  .card {
    position: absolute;
    top: 296px;
    width: 513px;
    height: 309px;
    box-sizing: border-box;
    overflow: hidden;
  }
  .card--front { left: 72px; background: var(--ink); }
  .card--back  { left: 615px; background: var(--paper); border: 2px solid var(--ink); }

  .edge-stripe {
    position: absolute;
    top: 0; right: 0;
    width: 22px; height: 100%;
    background: var(--amber);
  }
  .card--back .edge-stripe { right: 0; }

  .play-mark { position: absolute; top: 134px; width: 42px; height: 40px; }
  .card--front .play-mark { left: 465px; }
  .card--back  .play-mark { left: 463px; }

  .wordmark {
    position: absolute;
    display: flex;
    align-items: center;
    gap: 8px;
    font-family: "Didact Gothic", sans-serif;
    white-space: nowrap;
  }
  .wordmark__dot {
    width: 18px; height: 18px;
    border-radius: 50%;
    background: var(--kettle-red);
    flex: none;
  }
  .card--front .wordmark { left: 22px; top: 216px; font-size: 32px; color: var(--paper); }
  .card--back  .wordmark { left: 20px; top: 200px; font-size: 31px; color: var(--ink); }

  .tagline {
    position: absolute;
    left: 22px; top: 277px;
    margin: 0;
    font-family: "Open Sans", sans-serif;
    font-size: 20px;
    line-height: 1;
    color: var(--paper);
  }
  .tagline-rules { position: absolute; left: 22px; top: 265px; width: 340px; height: 22px; }

  .reel {
    position: absolute;
    border-radius: 50% 50% 40% 40%;
  }
  .card--front .reel {
    left: 378px; top: 199px; width: 105px; height: 97px;
    background: radial-gradient(circle at 40% 40%, var(--paper), var(--reel-light) 60%, #8a8a8a);
  }
  .card--back .reel {
    left: 367px; top: 191px; width: 113px; height: 105px;
    background: radial-gradient(circle at 40% 40%, #555, var(--reel-dark) 55%, var(--ink));
  }

  .company-name {
    position: absolute;
    right: 32px; top: 20px;
    margin: 0;
    font-family: "Arimo", sans-serif;
    font-size: 22px;
    color: var(--ink);
  }
  .logo-rule {
    position: absolute;
    left: 20px; top: 240px;
    width: 240px; height: 2px;
    background: var(--amber);
  }
  .contact {
    position: absolute;
    left: 20px; top: 246px;
    margin: 0;
    font-family: "Arimo", sans-serif;
    font-size: 16px;
    line-height: 18px;
    color: var(--ink);
    font-style: normal;
  }
</style>
</head>
<body>
<main class="canvas">

  <section class="card card--front" aria-label="Card front">
    <div class="edge-stripe"></div>
    <svg class="play-mark" viewBox="0 0 42 40"><polygon points="0,0 42,20 0,40" fill="var(--paper)"/></svg>
    <div class="wordmark"><span class="wordmark__dot"></span>Red Kettle Pictures</div>
    <svg class="tagline-rules" viewBox="0 0 340 22">
      <rect x="0" y="0" width="296" height="5" fill="var(--amber)"/>
      <rect x="198" y="10" width="128" height="4" fill="var(--amber)"/>
      <polygon points="332,4 334,10 340,10 335,14 337,20 332,16 327,20 329,14 324,10 330,10" fill="var(--amber)"/>
    </svg>
    <p class="tagline">Stories that matter</p>
    <div class="reel" role="img" aria-label="Film reel illustration"></div>
  </section>

  <section class="card card--back" aria-label="Card back">
    <div class="edge-stripe"></div>
    <svg class="play-mark" viewBox="0 0 42 40"><polygon points="0,0 42,20 0,40" fill="var(--ink)"/></svg>
    <p class="company-name">Red Kettle Pictures, LLC</p>
    <div class="wordmark"><span class="wordmark__dot"></span>Red Kettle Pictures</div>
    <div class="logo-rule"></div>
    <address class="contact">
      dorianne pasko<br>
      dP@RedKettlePix.example<br>
      407-555-0148
    </address>
    <div class="reel" role="img" aria-label="Film reel illustration"></div>
  </section>

</main>
</body>
</html>
```